Soccer Club Site Redesign

We are a suburban youth soccer club in need of a web site redesign. Our current site’s look/feel is outdated and is in need of a more modern look. What we are looking for is a design layout that will accommodate the current functionality we have for the site and give us an updated modern look. The deliverable for this project will be .psd file that can be converted to an html theme file for Wordpress. We will take care of the conversion and handle the html coding/javascript functionality.
Take a look at our current site to get an idea of what we offer and the current layout we have.
http://www.fernwickfootball.org
Our club hosts youth recreational soccer, traveling soccer and two large soccer tournaments during the year. We also sponsor a number of training clinics. Our site serves a couple primary purposes:
1. Parents learn how/where/when to sign up their child for the leagues we offer.
2. Parents learn dates/times of various events the club offers.
3. Other soccer clubs get information on the tournaments we offer, sign up for the tournaments etc.
We do a pretty good job of presenting information about the various events/leagues available and how to sign up for them, but we want to do a better job of presenting a calendar where parents can quickly find dates/times of various events. Ideally, we would like to incorporate a news section (like we currently have), with a calendar and the use of more images on the home page. We understand screen space is limited but would incorporate jquery/javascript widgets to hide/show info and maybe an ‘imagebox’ for the additional images.
Here are a few sites with ideas that we liked:
http://sports.dorrington.edu/ (Look at the Upcoming Events calendar on the page)
http://www.ashvalekickers.com/ (look at the Upcoming Events calendar in the right column and the image box in the main content area)
http://www.plumetfutbol.com/index.php (Like the look and use of images)
http://www.rqkickersclub.com/ (imagebox use)
http://www.lorvanpuckclub.org/ ( hockey website but like the use of crisp header graphics)
http://www.ellisfordpuck.com/ (another hockey site, like the calendar used)
That should give you a pretty good idea of what we are looking for. The new design will need to accommodate the existing functionality of the site. Our logo (which is attached) should be incorporated into the site….otherwise we are open to your design ideas.

```html
<!DOCTYPE html>
<html lang="en">
<head>
<meta charset="utf-8">
<title>Fernwick Soccer Club</title>
<link href="https://fonts.googleapis.com/css2?family=Patua+One&family=Roboto+Condensed:wght@400;700&family=Arimo:wght@400;700&display=swap" rel="stylesheet">
<style>
:root{
  --navy:#23378c;
  --nav-blue:#2a4a9e;
  --nav-border:#4a68b8;
  --gold:#f9c21c;
  --orange:#f6a43a;
  --orange-dark:#e88a1e;
  --red:#e0261a;
  --link:#1f4fa8;
  --text:#222;
  --sky-top:#e2edfb;
  --sky-bottom:#64a6f5;
  --panel:#ffffff;
  --event-bg:#f4f4f4;
}
*{box-sizing:border-box;margin:0;padding:0}
html,body{width:1200px;height:1034px;overflow:hidden}
body{
  position:relative;
  font-family:"Arimo",Arial,sans-serif;
  color:var(--text);
  background:linear-gradient(180deg,var(--sky-top) 0%,#cfe1f9 30%,#9cc5f7 60%,var(--sky-bottom) 70%,var(--sky-bottom) 100%);
}
.abs{position:absolute}

/* header */
.brand{left:150px;top:12px;display:flex;align-items:center;gap:14px}
.brand-mark{width:78px;height:78px;background:var(--navy);border-radius:6px}
.brand-name{font-family:"Patua One",Georgia,serif;font-size:41px;color:var(--navy);letter-spacing:.5px;padding-top:12px}
.social{top:28px;display:flex;align-items:center;justify-content:center;width:112px;height:28px;border-radius:3px;color:#fff;font-family:"Roboto Condensed",Arial,sans-serif;font-weight:700;font-size:13px;letter-spacing:.5px}
.social.chirp{left:793px;background:#3ec2ef}
.social.friend{left:923px;background:#3f5ea8}
.top-links{right:152px;top:82px;font-size:12.5px;color:#111}
.top-links a{color:#111;text-decoration:none}
.top-links span{margin:0 5px}

/* navigation */
.main-nav{left:153px;top:112px;width:894px;height:41px;background:var(--nav-blue);display:flex}
.main-nav a{font-family:"Roboto Condensed",Arial,sans-serif;font-size:16px;color:#fff;text-decoration:none;display:flex;align-items:center;justify-content:center;border-right:1px solid var(--nav-border);white-space:nowrap}
.main-nav a:last-child{border-right:none}
.main-nav a.active{background:var(--gold);color:#222}

/* panel */
.panel{left:153px;top:153px;width:894px;height:820px;background:var(--panel)}
.panel-base{left:153px;top:965px}

/* slider */
.slide{left:162px;top:167px;width:594px;height:284px;background:linear-gradient(135deg,#2c2c2c 0%,#5a5a5a 35%,#2a48b8 60%,#1b2f86 80%,#1c1c1c 100%)}
.slide-caption{left:162px;top:412px;width:594px;height:39px;background:rgba(40,40,40,.55);color:#fff;font-size:16px;padding:10px 13px}
.thumbs{left:162px;top:457px;display:flex;gap:15px}
.thumb{width:86px;height:62px;border:1px solid #ccc;padding:2px;background:#fff}
.thumb div{width:100%;height:100%;background:linear-gradient(180deg,#1a1a1a 0%,#334 45%,#3d7a2c 80%,#4f9a36 100%)}

/* events */
.events-title{left:778px;top:163px;font-family:"Roboto Condensed",Arial,sans-serif;font-weight:400;font-size:19px;color:var(--navy)}
.events{left:779px;top:192px;width:252px;height:382px;border:1px solid #c9c9c9;border-radius:4px;background:var(--event-bg);box-shadow:0 4px 4px rgba(0,0,0,.15);padding:9px 6px}
.event{display:flex;gap:10px;margin-bottom:8px}
.date{flex:none;width:35px;height:40px;background:var(--nav-blue);color:#fff;text-align:center;font-family:"Roboto Condensed",Arial,sans-serif;line-height:1;padding-top:5px;margin-top:4px}
.date b{display:block;font-size:15px}
.date small{font-size:13px}
.event p{font-size:11.3px;line-height:16px;color:#111}
.event a{display:block;font-size:11.3px;line-height:16px;color:var(--link);text-decoration:none;margin-top:2px}

/* register strip */
.strip{left:162px;top:602px;width:877px;height:35px}
.strip-label{top:603px;font-family:"Roboto Condensed",Arial,sans-serif;font-size:13px;color:#222;height:34px;display:flex;align-items:center;white-space:nowrap;letter-spacing:-.1px}
.register{top:596px;height:45px;background:var(--gold);border-radius:3px;color:var(--red);font-family:"Roboto Condensed",Arial,sans-serif;font-size:15.5px;display:flex;align-items:center;justify-content:center;box-shadow:0 2px 2px rgba(0,0,0,.12);white-space:nowrap}

/* article */
.article{left:164px;top:668px;width:594px}
.article h1{font-family:"Patua One",Georgia,serif;font-weight:400;font-size:19px;color:var(--navy);margin-bottom:12px;white-space:nowrap}
.article p{font-size:11.1px;line-height:19.7px;color:#222;margin-bottom:19px}
.article a{color:var(--red);font-size:13px;text-decoration:none;margin-left:6px}

/* sponsors */
.sponsors{left:779px;top:664px;width:259px;height:288px;border:1px solid #a9a9a9;background:#fff}
.sponsor{position:absolute;left:50%;transform:translateX(-50%)}
.sp-club{top:10px;width:80px;height:92px;background:var(--navy);border-radius:6px 6px 40px 40px}
.sp-assoc{top:125px;width:88px;height:60px;background:#2f5fb0;border-radius:4px}
.sp-kit{top:205px;width:88px;height:60px;background:#111;border-radius:4px}

.copyright{left:0;top:999px;width:1200px;text-align:center;font-size:12px;color:#111}
</style>
</head>
<body>

<header>
  <div class="abs brand">
    <div class="brand-mark"></div>
    <div class="brand-name">Fernwick Soccer Club</div>
  </div>
  <a class="abs social chirp">CHIRPNET</a>
  <a class="abs social friend">FRIENDBOOK</a>
  <nav class="abs top-links">
    <a href="#">Home</a><span>/</span><a href="#">About us</a><span>/</span><a href="#">Contact us</a><span>/</span><a href="#">Sponsers</a>
  </nav>
</header>

<nav class="abs main-nav">
  <a class="active" style="width:55px">Forms</a>
  <a style="width:80px">Calendar</a>
  <a style="width:87px">Travelling</a>
  <a style="width:102px">Recreational</a>
  <a style="width:97px">Tournaments</a>
  <a style="width:73px">Referees</a>
  <a style="width:85px">Field Maps</a>
  <a style="width:70px">Coaches</a>
  <a style="width:109px">Team Manager</a>
  <a style="width:85px">Volunteers</a>
  <a style="width:51px">Links</a>
</nav>

<div class="abs panel"></div>
<svg class="abs panel-base" width="894" height="40" viewBox="0 0 894 40" aria-hidden="true">
  <path d="M0 0 H894 V20 Q894 32 880 31 Q447 -10 14 31 Q0 32 0 20 Z" fill="#ffffff"/>
</svg>

<main>
  <div class="abs slide" role="img" aria-label="Action photo of two girls' soccer players competing for the ball at a night match"></div>
  <div class="abs slide-caption">Tittle Comes here</div>
  <div class="abs thumbs">
    <div class="thumb"><div role="img" aria-label="Thumbnail of players in a match"></div></div>
    <div class="thumb"><div role="img" aria-label="Thumbnail of players in a match"></div></div>
    <div class="thumb"><div role="img" aria-label="Thumbnail of players in a match"></div></div>
    <div class="thumb"><div role="img" aria-label="Thumbnail of players in a match"></div></div>
    <div class="thumb"><div role="img" aria-label="Thumbnail of players in a match"></div></div>
    <div class="thumb"><div role="img" aria-label="Thumbnail of players in a match"></div></div>
  </div>

  <h2 class="abs events-title">Upcoming Events</h2>
  <section class="abs events">
    <div class="event"><div class="date"><b>NOV</b><small>1st</small></div>
      <div><p>Fernwick High School Boys and Girls teams both win State Quarters to move to the final 4 at the Riverdome!</p><a href="#">Read more...</a></div></div>
    <div class="event"><div class="date"><b>NOV</b><small>1st</small></div>
      <div><p>NRYSA Fall State Champion and Fall League Champions</p><a href="#" style="margin-top:5px">Read more...</a></div></div>
    <div class="event"><div class="date"><b>NOV</b><small>1st</small></div>
      <div><p>Summer Travel 2013 - Roster Spots open: U11 and U12 Girls C3, U13 Boys C3 and U14 Girls C2</p><a href="#">Read more...</a></div></div>
    <div class="event" style="margin-top:12px"><div class="date"><b>NOV</b><small>1st</small></div>
      <div><p>Dana Halvorsen Memorial Youth Soccer Scholarship</p><a href="#">Read more...</a></div></div>
    <div class="event" style="margin-top:18px"><div class="date"><b>NOV</b><small>1st</small></div>
      <div><p>2013 Summer Travel Registration / Team Formations</p><a href="#">Read more...</a></div></div>
  </section>

  <svg class="abs strip" viewBox="0 0 877 35" width="877" height="35" aria-hidden="true">
    <path d="M10 0 H867 L877 17.5 L867 35 H10 L0 17.5 Z" fill="#f6a43a"/>
    <path d="M10 0 H867 L877 17.5 L867 35 H10 L0 17.5 Z" fill="none" stroke="#e88a1e" stroke-width="1"/>
  </svg>
  <div class="abs strip-label" style="left:174px">2013 Travel Soccer</div>
  <a class="abs register" style="left:287px;width:113px">REGISTER NOW</a>
  <div class="abs strip-label" style="left:409px">2013 Travel Soccer Waiting List</div>
  <a class="abs register" style="left:584px;width:113px">REGISTER NOW</a>
  <div class="abs strip-label" style="left:703px">2012 Fall Recreational Soccer League</div>
  <a class="abs register" style="left:906px;width:113px">REGISTER NOW</a>

  <article class="abs article">
    <h1>2013 Summer Travel Registration/Team Formations</h1>
    <p>The 2013 team formation process is now underway. All players should be contacted within 4 weeks of the try-out that they attended. Pre-registered players will be added to teams as roster space allows. Registration is now open for 2013 Summer Travel Soccer. Once you are contacted by your team coach you can go ahead and register. Please be sure to select the correct team/coach from the drop down when registering.</p>
    <p>Fees for 2013 remain the same as 2012 if you register by the early bird discount date of November 1st 2012 ($225 registration and $75 uniform fee). There will be new FSC uniforms for 2013 so all players are required to purchase a new FSC uniform set at the time of registering. After the early bird discount date of Nov 1st 2012, the regular fee of $350 ($275 registration and $75 uniform fee) will apply. <a href="#">To Register please click here.</a></p>
  </article>

  <aside class="abs sponsors">
    <div class="sponsor sp-club"></div>
    <div class="sponsor sp-assoc"></div>
    <div class="sponsor sp-kit"></div>
  </aside>
</main>

<footer class="abs copyright">Copyright © Fernwick Soccer Club 2012. All Rights reserved</footer>

</body>
</html>
```